Business Card Design

I need a good card to sell my talents in the music field and get my name known as a musician/Guitarist

Industry/Entity Type

Business

Contact Information for Business Card

Nathaniel Brisco Musician/Guitarist

```html
<!DOCTYPE html>
<html lang="en">
<head>
<meta charset="UTF-8">
<title>Nathaniel Brisco – Business Card</title>
<link rel="stylesheet" href="https://fonts.googleapis.com/css2?family=Nunito+Sans:ital,wght@0,300;0,700;1,400&display=swap">
<style>
  :root {
    --paper: #ffffff;
    --ink: #000000;
    --band-top: 351px;
  }
  html, body {
    margin: 0;
    padding: 0;
    width: 1200px;
    height: 704px;
    overflow: hidden;
    background: var(--paper);
  }
  .card {
    position: relative;
    width: 1200px;
    height: 704px;
    overflow: hidden;
    background: var(--paper);
    font-family: "Nunito Sans", sans-serif;
  }
  .lower-band {
    position: absolute;
    left: 0;
    top: var(--band-top);
    width: 100%;
    height: calc(704px - var(--band-top));
    background: var(--ink);
  }
  .identity {
    position: absolute;
    left: 109px;
    top: 90px;
    color: var(--ink);
  }
  .identity__name {
    margin: 0;
    font-size: 54px;
    font-weight: 700;
    line-height: 62px;
    letter-spacing: 0.2px;
  }
  .identity__role {
    margin: 0;
    font-size: 49px;
    font-style: italic;
    font-weight: 400;
    line-height: 58px;
  }
  .contact {
    position: absolute;
    left: 109px;
    top: 396px;
    color: var(--paper);
    font-size: 33px;
    font-weight: 300;
    line-height: 46px;
    letter-spacing: 0.3px;
  }
  .contact__row {
    display: flex;
  }
  .contact__label {
    width: 196px;
  }
  .contact__address {
    margin: 42px 0 0;
    line-height: 44px;
  }
  .brand-name {
    position: absolute;
    left: 938px;
    top: 420px;
    width: 240px;
    text-align: center;
    color: var(--paper);
    font-size: 32px;
    font-weight: 700;
    line-height: 40px;
  }
</style>
</head>
<body>
  <main class="card">
    <div class="lower-band"></div>

    <header class="identity">
      <h1 class="identity__name">Nathaniel Brisco</h1>
      <p class="identity__role">Musician / Guitarist</p>
    </header>

    <section class="contact">
      <div class="contact__row"><span class="contact__label">Cell:</span><span>845-555-0182</span></div>
      <div class="contact__row"><span class="contact__label">Email:</span><span>yourname@yourdomain.com</span></div>
      <p class="contact__address">482 Alder Brook Road Millbrook Hollow,<br>N.Y. 10977</p>
    </section>

    <div class="brand-name">Brisco Sound</div>
  </main>
</body>
</html>
```